Business Card for Industrial Distributor

We need a business card design for an industrial distributor. We sell machine parts for the manufacturing and oil industry. We would like the cards to look clean and modern but with a touch of industry.

Our colors are blue/white.

Please feel free to visit our website www.korvanlineusa.com

Target Market(s)

mexican manufacturers in the automobile/aerospace industry

Industry/Entity Type

Industrial

Colors
ffffff
0555a3

```html
<!DOCTYPE html>
<html lang="en">
<head>
<meta charset="utf-8">
<title>Korvanline Business Card</title>
<link rel="stylesheet" href="https://fonts.googleapis.com/css2?family=Open+Sans:wght@400;600;700;800&display=swap">
<style>
  :root {
    --page-bg: #2b2b2d;
    --navy: #25287a;
    --brand-blue: #0555a3;
    --accent-blue: #1f7fd0;
    --label-blue: #5aa9e6;
    --white: #ffffff;
    --light-grey: #eceef1;
    --mid-grey: #d4d7dc;
    --back-dark: #070d24;
    --back-mid: #16307a;
  }
  * { box-sizing: border-box; margin: 0; padding: 0; }
  html, body { width: 1200px; height: 900px; overflow: hidden; }
  body {
    background: var(--page-bg);
    font-family: "Open Sans", Arial, sans-serif;
    position: relative;
  }
  .card {
    position: absolute;
    width: 640px;
    height: 366px;
    border-radius: 22px;
    overflow: hidden;
  }
  /* Back side */
  .card-back { left: 120px; top: 70px; }
  .card-back .gear-artwork {
    position: absolute; inset: 0;
    background: radial-gradient(circle at 62% 55%, var(--back-mid) 0%, #0d1c4f 45%, var(--back-dark) 100%);
  }
  .card-back .brand {
    position: absolute; left: 300px; top: 150px;
    display: flex; align-items: center; gap: 16px;
  }
  .card-back .brand-dot {
    width: 58px; height: 58px; border-radius: 50%;
    background: var(--white);
  }
  .card-back .brand-name {
    color: var(--white); font-weight: 800; font-size: 44px; letter-spacing: -0.5px;
  }
  /* Front side */
  .card-front { left: 440px; top: 470px; background: var(--light-grey); }
  .card-front .gear-pattern {
    position: absolute; left: 0; top: 0; width: 100%; height: 260px;
    background: linear-gradient(160deg, var(--white) 0%, var(--light-grey) 55%, var(--mid-grey) 100%);
  }
  .card-front .band { position: absolute; inset: 0; }
  .card-front .brand {
    position: absolute; left: 36px; top: 38px;
    display: flex; align-items: center; gap: 18px;
  }
  .card-front .brand-dot {
    width: 70px; height: 70px; border-radius: 50%;
    background: var(--brand-blue);
  }
  .card-front .brand-name {
    color: var(--navy); font-weight: 800; font-size: 60px; letter-spacing: -1px; line-height: 1;
  }
  .person {
    position: absolute; left: 40px; top: 176px;
    font-weight: 700; font-size: 15px; line-height: 19px;
  }
  .person .name { color: var(--accent-blue); }
  .person .role { color: var(--navy); }
  .contact {
    position: absolute; left: 40px; top: 268px;
    list-style: none; color: var(--white); font-size: 15px; line-height: 21px;
  }
  .contact .label { color: var(--label-blue); font-weight: 700; display: inline-block; width: 14px; }
  .address {
    position: absolute; right: 40px; top: 170px;
    color: #dfe4f2; font-size: 14px; line-height: 20px; text-align: right;
  }
</style>
</head>
<body>
  <section class="card card-back" aria-label="Card back">
    <div class="gear-artwork" role="img" aria-label="Photograph of interlocking blue steel gears"></div>
    <div class="brand">
      <span class="brand-dot"></span>
      <span class="brand-name">Korvanline</span>
    </div>
  </section>

  <section class="card card-front" aria-label="Card front">
    <div class="gear-pattern" role="img" aria-label="Faint grey gear pattern"></div>
    <svg class="band" viewBox="0 0 640 366" width="640" height="366" aria-hidden="true">
      <defs>
        <linearGradient id="bandFill" x1="0" y1="0" x2="0" y2="1">
          <stop offset="0" stop-color="#2e3290"/>
          <stop offset="1" stop-color="#1f2270"/>
        </linearGradient>
      </defs>
      <path d="M0,232 C210,262 430,210 640,100 L640,366 L0,366 Z" fill="url(#bandFill)"/>
      <path d="M170,240 C360,236 500,180 640,92" fill="none" stroke="var(--brand-blue)" stroke-width="6" stroke-linecap="round"/>
    </svg>
    <div class="brand">
      <span class="brand-dot"></span>
      <span class="brand-name">Korvanline</span>
    </div>
    <p class="person">
      <span class="name">Daniel Reyes</span><br>
      <span class="role">managing director</span>
    </p>
    <ul class="contact">
      <li><span class="label">P</span> (555) 310 4827</li>
      <li><span class="label">F</span> (555) 310 4831</li>
      <li><span class="label">E</span> d.reyes@korvanlineusa.com</li>
    </ul>
    <p class="address">
      4120 Harbor Mill Rd<br>
      Corvale, TX 78500<br>
      www.korvanlineusa.com
    </p>
  </section>
</body>
</html>
```